Brochure Annual Report Design

I want to create a brochure / annual report for our company. Can you help me. I like this design. https://pixelstallhub.com/Brightfold/2847163-Annual-Report-2018. Here is our company website www.velmordental.com. Please take the logo from there. Our website needs an upgrade in how it looks. I would like the brochure annual report and the website to look somewhat congruent. I also want to create a very high end magazine that is fun for our company eventually.

We are a company that helps dentists create better practices by really improving the way they do business and motivating their teams. As a result they have more fun, more profit, happier team members, and they all have better lives.

Target Market(s)

dentist

Industry/Entity Type

Dental

Number of Pages Required

5+ page

Colors
0255a3
85cae6
ffffff

Requirements
Must have
• Must look really good.
Nice to have
• Any creative suggestions are welcomed. I need a website that looks congruent to the brochure and annual report. I also want to create a very high end magazine that is fun for our company eventually.
Should not have
• I don't like low quality design.

```html
<!DOCTYPE html>
<html lang="en">
<head>
<meta charset="utf-8">
<title>Velmor Dental — Annual Report 2018</title>
<link href="https://fonts.googleapis.com/css2?family=Montserrat:wght@400;500;600;700;800&display=swap" rel="stylesheet">
<style>
:root{
  --blue-deep:#0255a3;
  --blue-mid:#1677c9;
  --blue-light:#85cae6;
  --blue-pale:#c3e6f5;
  --white:#ffffff;
  --ink:#1e1e1e;
  --grey-text:#6b6b6b;
  --grey-box:#f1f1f1;
  --stage:#3b3b3b;
}
*{margin:0;padding:0;box-sizing:border-box}
html,body{width:1200px;height:1200px;overflow:hidden;background:var(--stage);font-family:'Montserrat',sans-serif;color:var(--ink)}
.spread{position:absolute;width:570px;height:400px;background:var(--white);overflow:hidden}
.spread--about{left:20px;top:120px}
.spread--team{left:610px;top:120px}
.spread--contents{left:315px;top:680px}
.header-art{position:absolute;left:0;top:0}
.report-tag{position:absolute;left:14px;top:24px;font-size:5px;color:var(--white);line-height:1.15}
.brand{position:absolute;right:18px;top:24px;display:flex;align-items:center;gap:4px}
.brand-name{font-size:9px;font-weight:600;color:var(--ink)}
.brand-square{width:5px;height:5px;background:var(--blue-deep)}
.gutter{position:absolute;left:285px;top:170px;width:1px;height:210px;background:#f0f0f0}
.footer{position:absolute;top:382px;font-size:3.5px;color:var(--grey-text);display:flex;align-items:center;gap:6px}
.footer--left{left:18px}
.footer--right{right:18px}
.footer-rule{width:210px;height:1px;background:var(--blue-pale)}
.body{font-size:4.6px;line-height:1.55;color:var(--grey-text);text-align:justify}
/* About */
.about-title{position:absolute;left:45px;top:170px;font-size:23px;font-weight:800;color:var(--ink)}
.about-rule{position:absolute;left:45px;top:206px;width:28px;height:2px;background:var(--blue-light)}
.about-intro{position:absolute;left:80px;top:203px;width:160px}
.portrait{position:absolute;left:40px;top:260px;width:118px;height:102px}
.leader{position:absolute;left:170px;top:272px}
.leader-name{font-size:7px;font-weight:700}
.leader-role{font-size:4px;color:var(--blue-light);margin-top:2px}
.leader-rule{width:66px;height:1px;background:var(--blue-pale);margin-top:6px}
.accent-bar{position:absolute;left:170px;top:337px;width:380px;height:25px;background:var(--blue-pale)}
.about-col{position:absolute;top:188px;width:112px}
.about-col--one{left:318px}
.about-col--two{left:440px}
.about-col p{margin-bottom:5px}
.drop-cap{float:left;font-size:20px;line-height:16px;color:var(--blue-deep);margin-right:2px;font-weight:400}
/* Team */
.member{position:absolute;top:170px;width:118px}
.member-head{display:flex;align-items:flex-start;gap:6px;height:44px}
.member-photo{width:40px;height:40px;flex:none}
.member-name{font-size:6px;font-weight:700;margin-top:12px}
.member-role{font-size:3.6px;color:var(--blue-light);margin-top:1px;line-height:1.3}
.member-rule{height:1px;background:var(--blue-pale);margin-top:2px}
.member .body{margin-top:12px;height:64px}
.quote{background:var(--grey-box);padding:6px 6px 5px;margin-top:10px;border-bottom:1px solid var(--blue-pale)}
.quote-head{display:flex;gap:4px;font-size:4.6px;font-weight:500;line-height:1.3}
.quote-mark{font-size:15px;color:var(--blue-light);line-height:10px;font-weight:800}
.quote .body{margin-top:5px;height:auto;font-size:3.6px}
/* Contents */
.contents-title{position:absolute;left:0;width:570px;text-align:center;top:82px;font-size:36px;font-weight:800;color:#4a4a4a;letter-spacing:-.5px}
.contents-col{position:absolute;top:180px;width:215px;list-style:none}
.contents-col--left{left:40px}
.contents-col--right{left:320px}
.entry{position:relative;padding-left:22px;height:19px}
.entry::before{content:"";position:absolute;left:0;top:3px;width:14px;height:1.5px;background:var(--blue-light)}
.entry-title{font-size:4.4px;font-weight:700;display:flex;gap:2px}
.entry-dots{flex:1;border-bottom:1px dotted #aaa;margin-bottom:1px}
.entry-sub{font-size:3.8px;color:var(--grey-text);margin-top:1px}
</style>
</head>
<body>

<svg width="0" height="0" style="position:absolute">
  <defs>
    <linearGradient id="roomTone" x1="0" y1="0" x2="1" y2="0">
      <stop offset="0" stop-color="#8f8f8f"/><stop offset=".5" stop-color="#b9b9b9"/><stop offset="1" stop-color="#9c9c9c"/>
    </linearGradient>
    <linearGradient id="skinTone" x1="0" y1="0" x2="0" y2="1">
      <stop offset="0" stop-color="#e8e8e6"/><stop offset="1" stop-color="#c9cfd6"/>
    </linearGradient>
  </defs>
</svg>

<!-- Spread: About -->
<section class="spread spread--about">
  <svg class="header-art" width="570" height="240" viewBox="0 0 570 240">
    <rect x="0" y="47" width="570" height="81" fill="url(#roomTone)" role="img" aria-label="Greyscale photo of a seminar room filled with dental team members"/>
    <polygon points="110,0 260,0 150,128 0,128 0,100" fill="var(--blue-light)" opacity=".85"/>
    <polygon points="0,50 125,50 0,205" fill="var(--blue-mid)" opacity=".9"/>
    <polygon points="0,95 70,95 0,190" fill="var(--blue-deep)"/>
    <polygon points="0,21 76,21 66,37 0,37" fill="var(--blue-deep)"/>
  </svg>
  <div class="report-tag">Annual Report<br>2018</div>
  <div class="brand"><span class="brand-square"></span><span class="brand-name">Velmor Dental</span></div>
  <div class="gutter"></div>

  <h1 class="about-title">About Us</h1>
  <div class="about-rule"></div>
  <p class="body about-intro">Dentistry is the greatest profession ever. The key to enjoying this great profession is to have the proper tools and to keep your team engaged around you. This is why we created Velmor Dental: to bring you proven practices and tools that keep your team motivated.</p>
  <svg class="portrait" viewBox="0 0 118 102" role="img" aria-label="Portrait photo of the founder"><rect width="118" height="102" fill="url(#skinTone)"/></svg>
  <div class="leader"><div class="leader-name">Grant Holloway</div><div class="leader-role">Founder &amp; CEO</div><div class="leader-rule"></div></div>
  <div class="accent-bar"></div>

  <div class="body about-col about-col--one">
    <p><span class="drop-cap">G</span>rant Holloway speaks and consults with dentists across the world on how to create a better practice and a better life. He is one of the leading seminar speakers and online education experts. He has invested more than twenty years in his profession and in refining the best systems and practices within the dental field.</p>
    <p>Grant has spoken at nearly every major dental meeting in the country. His company has been named one of the top dental consultants for the last ten years by Practice Leaders Weekly, and one of the fastest growing firms in the region. His team offers trusted advisors to each dentist they serve.</p>
  </div>
  <div class="body about-col about-col--two">
    <p>He and his team are committed to bringing valuable solutions that preserve the great profession of dentistry in ways that are easily understood, widely applicable and genuinely fun. Entertainment is a mantra here, and our video show has been watched by dentists all over the world.</p>
    <p>In 2017 Grant and his team created one of the first live podcast video shows in dentistry. Today it is one of the most widely viewed dental education resources, with thousands of followers and listeners.</p>
    <p>When he is not inspiring dentists and their teams, he is coaching or watching his kids play sports, or at home doing what he loves most: spending time with his family.</p>
  </div>

  <div class="footer footer--left">2 &nbsp; ANNUAL REPORT 2017 <span class="footer-rule"></span></div>
  <div class="footer footer--right"><span class="footer-rule"></span>2017 ANNUAL REPORT &nbsp; 3</div>
</section>

<!-- Spread: Team -->
<section class="spread spread--team">
  <svg class="header-art" width="570" height="240" viewBox="0 0 570 240">
    <rect x="0" y="47" width="570" height="81" fill="url(#roomTone)" role="img" aria-label="Greyscale photo of a seminar audience facing a speaker"/>
    <polygon points="110,0 260,0 150,128 0,128 0,100" fill="var(--blue-light)" opacity=".85"/>
    <polygon points="0,50 125,50 0,205" fill="var(--blue-mid)" opacity=".9"/>
    <polygon points="0,95 70,95 0,190" fill="var(--blue-deep)"/>
    <polygon points="0,21 76,21 66,37 0,37" fill="var(--blue-deep)"/>
  </svg>
  <div class="report-tag">Annual Report<br>2018</div>
  <div class="brand"><span class="brand-square"></span><span class="brand-name">Velmor Dental</span></div>
  <div class="gutter"></div>

  <article class="member" style="left:18px">
    <div class="member-head"><svg class="member-photo" role="img" aria-label="Portrait photo of team member"><rect width="40" height="40" fill="url(#skinTone)"/></svg><div><div class="member-name">Marissa Quinlan</div><div class="member-role">Lead Practice Coach &amp;<br>Events Coordinator</div><div class="member-rule"></div></div></div>
    <p class="body">Marissa has been involved in dentistry since 1985. Over the years she has held many positions on the dental team, including dental assistant, business office and hygienist. Her wide knowledge of the front office and clinical procedures is a great asset, and she loves to help teams do their best work.</p>
    <div class="quote"><div class="quote-head"><span class="quote-mark">“</span>I have three favorite things about working at Velmor:</div><p class="body">The people, they always make me laugh. Every day is a new adventure. Finally, I love hearing the stories of our clients.</p></div>
  </article>
  <article class="member" style="left:150px">
    <div class="member-head"><svg class="member-photo" role="img" aria-label="Portrait photo of team member"><rect width="40" height="40" fill="url(#skinTone)"/></svg><div><div class="member-name">Dana Ellery</div><div class="member-role">Director of Coaching</div><div class="member-rule"></div></div></div>
    <p class="body">Dana brings strong organizational and financial skills from her years as a business owner and sales representative. She joined the team in April 2012 and is the heart of our home office in Lakemont. She holds a degree in business administration.</p>
    <div class="quote"><div class="quote-head"><span class="quote-mark">“</span>I have three favorite things about working at Velmor:</div><p class="body">The people, they always make me laugh. Every day is a new adventure. Finally, I love hearing the stories of our clients.</p></div>
  </article>
  <article class="member" style="left:305px">
    <div class="member-head"><svg class="member-photo" role="img" aria-label="Portrait photo of team member"><rect width="40" height="40" fill="url(#skinTone)"/></svg><div><div class="member-name">Marissa Quinlan</div><div class="member-role">Lead Practice Coach &amp;<br>Events Coordinator</div><div class="member-rule"></div></div></div>
    <p class="body">Marissa has been involved in dentistry since 1985. Over the years she has held many positions on the dental team, including dental assistant, business office and hygienist. Her wide knowledge of the front office and clinical procedures is a great asset, and she loves to help teams do their best work.</p>
    <div class="quote"><div class="quote-head"><span class="quote-mark">“</span>I have three favorite things about working at Velmor:</div><p class="body">The people, they always make me laugh. Every day is a new adventure. Finally, I love hearing the stories of our clients.</p></div>
  </article>
  <article class="member" style="left:437px">
    <div class="member-head"><svg class="member-photo" role="img" aria-label="Portrait photo of team member"><rect width="40" height="40" fill="url(#skinTone)"/></svg><div><div class="member-name">Joanne Pell</div><div class="member-role">Lead Practice Coach</div><div class="member-rule"></div></div></div>
    <p class="body">Joanne brings strong organizational and financial skills from her years as a business owner and sales representative. She joined the team in April 2012 and is a key part of our home office in Lakemont. She holds a degree in business administration.</p>
    <div class="quote"><div class="quote-head"><span class="quote-mark">“</span>I have three favorite things about working at Velmor:</div><p class="body">The people, they always make me laugh. Every day is a new adventure. Finally, I love hearing the stories of our clients.</p></div>
  </article>

  <div class="footer footer--left">4 &nbsp; ANNUAL REPORT 2017 <span class="footer-rule"></span></div>
  <div class="footer footer--right"><span class="footer-rule"></span>2017 ANNUAL REPORT &nbsp; 5</div>
</section>

<!-- Spread: Contents -->
<section class="spread spread--contents">
  <svg class="header-art" width="570" height="240" viewBox="0 0 570 240">
    <rect x="0" y="47" width="570" height="81" fill="url(#roomTone)" role="img" aria-label="Greyscale photo of a seminar room with a presenter"/>
    <polygon points="110,0 260,0 150,128 0,128 0,100" fill="var(--blue-light)" opacity=".85"/>
    <polygon points="0,50 125,50 0,205" fill="var(--blue-mid)" opacity=".9"/>
    <polygon points="0,95 70,95 0,190" fill="var(--blue-deep)"/>
    <polygon points="0,21 76,21 66,37 0,37" fill="var(--blue-deep)"/>
  </svg>
  <div class="report-tag">Annual Report<br>2018</div>
  <div class="brand"><span class="brand-square"></span><span class="brand-name">Velmor Dental</span></div>
  <h1 class="contents-title">Table of Content</h1>

  <ol class="contents-col contents-col--left">
    <li class="entry"><div class="entry-title">A message from our founder<span class="entry-dots"></span>01</div><div class="entry-sub">Why we do what we do for dentists</div></li>
    <li class="entry"><div class="entry-title">Our mission and our values<span class="entry-dots"></span>02</div><div class="entry-sub">Better practice, better life for every team</div></li>
    <li class="entry"><div class="entry-title">The year in review<span class="entry-dots"></span>03</div><div class="entry-sub">Key moments and milestones of the year</div></li>
    <li class="entry"><div class="entry-title">Meet our coaching team<span class="entry-dots"></span>04</div><div class="entry-sub">The people behind every success story</div></li>
    <li class="entry"><div class="entry-title">Client stories and results<span class="entry-dots"></span>05</div><div class="entry-sub">Practices that grew with our programs</div></li>
    <li class="entry"><div class="entry-title">Events and live seminars<span class="entry-dots"></span>06</div><div class="entry-sub">Where teams learn, laugh and connect</div></li>
    <li class="entry"><div class="entry-title">Podcast and online learning<span class="entry-dots"></span>07</div><div class="entry-sub">Episodes, views and new listeners</div></li>
    <li class="entry"><div class="entry-title">Leadership and team culture<span class="entry-dots"></span>08</div><div class="entry-sub">Tools for motivated, happier teams</div></li>
    <li class="entry"><div class="entry-title">Financial highlights<span class="entry-dots"></span>09</div><div class="entry-sub">Growth, profit and reinvestment</div></li>
    <li class="entry"><div class="entry-title">Looking ahead<span class="entry-dots"></span>10</div><div class="entry-sub">Our goals for the coming year</div></li>
  </ol>
  <ol class="contents-col contents-col--right">
    <li class="entry"><div class="entry-title">A message from our founder<span class="entry-dots"></span>01</div><div class="entry-sub">Why we do what we do for dentists</div></li>
    <li class="entry"><div class="entry-title">Our mission and our values<span class="entry-dots"></span>02</div><div class="entry-sub">Better practice, better life for every team</div></li>
    <li class="entry"><div class="entry-title">The year in review<span class="entry-dots"></span>03</div><div class="entry-sub">Key moments and milestones of the year</div></li>
    <li class="entry"><div class="entry-title">Meet our coaching team<span class="entry-dots"></span>04</div><div class="entry-sub">The people behind every success story</div></li>
    <li class="entry"><div class="entry-title">Client stories and results<span class="entry-dots"></span>05</div><div class="entry-sub">Practices that grew with our programs</div></li>
    <li class="entry"><div class="entry-title">Events and live seminars<span class="entry-dots"></span>06</div><div class="entry-sub">Where teams learn, laugh and connect</div></li>
    <li class="entry"><div class="entry-title">Podcast and online learning<span class="entry-dots"></span>07</div><div class="entry-sub">Episodes, views and new listeners</div></li>
    <li class="entry"><div class="entry-title">Leadership and team culture<span class="entry-dots"></span>08</div><div class="entry-sub">Tools for motivated, happier teams</div></li>
    <li class="entry"><div class="entry-title">Financial highlights<span class="entry-dots"></span>09</div><div class="entry-sub">Growth, profit and reinvestment</div></li>
    <li class="entry"><div class="entry-title">Looking ahead<span class="entry-dots"></span>10</div><div class="entry-sub">Our goals for the coming year</div></li>
  </ol>

  <div class="footer footer--left">6 &nbsp; ANNUAL REPORT 2017 <span class="footer-rule"></span></div>
  <div class="footer footer--right"><span class="footer-rule"></span>2017 ANNUAL REPORT &nbsp; 7</div>
</section>

</body>
</html>
```